job report

Designer – Professional Plumbing Job Report Template

Overview

We are seeking a skilled designer to create a professional, easy-to-use Job Report template for a commercial and maintenance plumbing business.
The report will be used for clients, property managers, facilities managers, strata, and retail centres and must clearly communicate findings, works completed, and recommendations in a polished, compliant, and branded format.

The final document must be suitable for PDF delivery, email, and ongoing reuse.

Objectives

Present plumbing works in a clear, professional, and defensible report format

Improve client understanding of findings and recommendations

Provide a repeatable template that can be used across maintenance, reactive, and investigative works

Allow easy insertion of text, tables, and photos

Report Structure (Minimum Inclusions)
1. Cover Page

Company logo and branding

Report title (e.g. Plumbing Job Report / Investigation Report)

Client name

Site address

Job reference / work order number

Date of attendance

Technician / contractor name

2. Client & Site Details

Client / company name

Site address

Contact person

Contact details

Access notes (after-hours, tenant access, etc.)

3. Reason for Attendance

Clear description of why attendance was required

Call-out type (reactive, scheduled maintenance, investigation, emergency, etc.)

Reported issue or scope requested by client

4. Findings / Observations

Detailed findings discovered on site

Condition of pipework, fixtures, drainage, or systems

Any contributing factors identified

Notes on compliance, wear, damage, or risk

(This section should support bullet points and paragraphs.)

5. Works Carried Out

Step-by-step description of works completed

Equipment used (e.g. jetter, CCTV camera, leak detection, flex shaft, etc.)

Repairs, replacements, testing, and verification

Confirmation that systems were tested and operational on completion

6. Photos & Visual Evidence

Clearly labelled photo sections

Before / during / after photos

Space for photo captions and explanations

Logical layout that aligns photos with written findings

7. Recommendations

Clearly separated from works completed

Urgent vs non-urgent recommendations

Preventative maintenance advice

Upgrade or replacement suggestions

Risk-based language where appropriate

8. Limitations & Exclusions

Areas not inspected

Access limitations

Assumptions made during inspection

Items outside scope of works

9. Conclusion

Summary of outcome

Confirmation of current system status

Next steps (if any)

10. Sign-Off

Contractor / technician name

Company name

Date

Optional client acknowledgement section

Design Requirements

Clean, professional layout

Commercial / trade-appropriate styling (not overly creative)

Easy-to-read fonts

Consistent headings and spacing

Logical flow for busy property managers

Editable format (Word / Google Docs / InDesign source file)

Final export-ready PDF version

Bonus (Nice to Have)

Traffic-light system (Green / Amber / Red) for condition reporting

Iconography for findings, repairs, and recommendations

Optional sections for compliance notes (AS/NCC references)

Space for QR codes or job reference numbers

Deliverables

Editable master report template

PDF version

Instructions or notes for ongoing use

```html
<!DOCTYPE html>
<html lang="en">
<head>
<meta charset="utf-8">
<title>Plumbing Job Report – Template Pages</title>
<link href="https://fonts.googleapis.com/css2?family=Lexend:wght@500;600&family=Montserrat:wght@400;500;700&display=swap" rel="stylesheet">
<style>
  :root {
    --blue: #29aedf;
    --yellow: #f1b42f;
    --beige: #efe9dc;
    --beige-light: #f6f2ea;
    --ink: #1c1c1c;
    --white: #ffffff;
    --line: #2a2a2a;
  }
  * { box-sizing: border-box; margin: 0; padding: 0; }
  html, body { width: 1200px; height: 530px; overflow: hidden; background: var(--white); }
  body { position: relative; font-family: "Montserrat", sans-serif; color: var(--ink); }

  .page { position: absolute; top: 29px; width: 364px; height: 472px; overflow: hidden; background: var(--blue); }
  .page--cover { left: 28px; }
  .page--client { left: 418px; }
  .page--reason { left: 807px; }

  .page__backdrop { position: absolute; inset: 0; width: 100%; height: 100%; }

  .page__photo { position: absolute; border-radius: 90px 90px 0 0; }
  .page--cover .page__photo { left: 150px; top: 190px; width: 214px; height: 282px;
    background: linear-gradient(180deg, #c9a68a 0%, #8e99a8 35%, #2f4fb3 65%, #e1962f 100%); }
  .page--client .page__photo { left: 130px; top: 168px; width: 220px; height: 304px;
    background: linear-gradient(180deg, #c49a80 0%, #25304f 35%, #1e2942 70%, #d9a43a 100%); }
  .page--reason .page__photo { left: 140px; top: 114px; width: 224px; height: 358px;
    background: linear-gradient(180deg, #c99a80 0%, #8e2a35 30%, #2f46b0 60%, #2b2b2b 100%); }

  .brand { position: absolute; left: 280px; top: 52px; width: 76px; text-align: center;
    font-family: "Montserrat", sans-serif; font-weight: 700; color: var(--blue);
    font-size: 13px; line-height: 14px; letter-spacing: 0.5px; }
  .brand__sub { display: block; font-size: 8.5px; letter-spacing: 1px; }

  .card { position: absolute; left: 16px; top: 15px; width: 191px; height: 353px;
    background: var(--white); border-radius: 6px; }
  .page--reason .card { height: 348px; }

  .card__title { position: absolute; left: 16px; font-family: "Lexend", sans-serif; font-weight: 600;
    font-size: 15.5px; line-height: 29px; color: var(--blue); text-transform: uppercase; }
  .card__title .accent { color: var(--yellow); }

  .field { position: absolute; left: 16px; width: 157px; height: 20px; border-bottom: 0.8px solid var(--line);
    font-size: 8px; font-weight: 500; text-transform: uppercase; display: flex; align-items: center; gap: 5px; }
  .field svg { width: 6px; height: 6px; flex: none; fill: var(--ink); }

  .group-label { position: absolute; left: 16px; font-size: 8px; font-weight: 500; text-transform: uppercase; }
  .check { position: absolute; left: 16px; font-size: 7px; font-weight: 500; text-transform: uppercase;
    display: flex; align-items: center; gap: 5px; }
  .check::before { content: ""; width: 6px; height: 6px; border: 0.8px solid var(--ink); border-radius: 1px; }

  .summary { position: absolute; left: 18px; top: 91px; width: 170px; font-size: 8px; line-height: 18px; }

  .cta { position: absolute; left: 15px; top: 432px; width: 100px; height: 26px; background: var(--white);
    border-radius: 13px; display: flex; align-items: center; gap: 9px; padding-left: 6px;
    font-size: 8px; font-weight: 500; letter-spacing: 0.4px; text-transform: uppercase; }
  .cta__dot { width: 17px; height: 17px; border-radius: 50%; background: var(--yellow);
    display: flex; align-items: center; justify-content: center; }
  .cta__dot svg { width: 7px; height: 7px; stroke: var(--ink); fill: none; stroke-width: 1.6; }
</style>
</head>
<body>

<svg width="0" height="0" style="position:absolute">
  <defs>
    <symbol id="icon-user" viewBox="0 0 10 10"><circle cx="5" cy="3" r="2.3"/><path d="M0.8 10 C1 6.5 9 6.5 9.2 10 Z"/></symbol>
    <symbol id="icon-pin" viewBox="0 0 10 10"><path d="M5 0 C2.4 0 1 2 1 3.8 C1 6.4 5 10 5 10 C5 10 9 6.4 9 3.8 C9 2 7.6 0 5 0 Z M5 2.4 A1.4 1.4 0 1 1 5 5.2 A1.4 1.4 0 1 1 5 2.4 Z" fill-rule="evenodd"/></symbol>
    <symbol id="icon-case" viewBox="0 0 10 10"><path d="M3.5 1.5 H6.5 V3 H9.5 V9 H0.5 V3 H3.5 Z M4.3 2.2 V3 H5.7 V2.2 Z" fill-rule="evenodd"/></symbol>
    <symbol id="icon-calendar" viewBox="0 0 10 10"><path d="M0.5 1.5 H9.5 V9.5 H0.5 Z M1.5 4 V8.5 H8.5 V4 Z" fill-rule="evenodd"/><rect x="2.5" y="5" width="1.4" height="1.2"/><rect x="4.3" y="5" width="1.4" height="1.2"/><rect x="6.1" y="5" width="1.4" height="1.2"/><rect x="2.5" y="6.8" width="1.4" height="1.2"/><rect x="4.3" y="6.8" width="1.4" height="1.2"/></symbol>
    <symbol id="icon-doc" viewBox="0 0 10 10"><path d="M1.5 0.5 H6.5 L8.5 2.5 V9.5 H1.5 Z"/></symbol>
    <symbol id="backdrop" viewBox="0 0 364 472" preserveAspectRatio="none">
      <polygon points="276,0 364,0 364,472 178,472" fill="#efe9dc"/>
      <polygon points="0,186 180,300 300,472 0,472" fill="#f1b42f"/>
      <polygon points="0,395 0,472 150,472" fill="#29aedf"/>
    </symbol>
  </defs>
</svg>

<!-- Cover page -->
<section class="page page--cover">
  <svg class="page__backdrop" aria-hidden="true"><use href="#backdrop"/></svg>
  <div class="page__photo" role="img" aria-label="Photo of a smiling plumber in blue overalls with a tool belt giving thumbs up"></div>
  <div class="brand">TIDEWAY<span class="brand__sub">PLUMBING</span></div>
  <div class="card">
    <h1 class="card__title" style="top:21px">Plumbing <span class="accent">Job</span><br>Report</h1>
    <div class="field" style="top:131px"><svg><use href="#icon-user"/></svg>Client Name</div>
    <div class="field" style="top:181px"><svg><use href="#icon-pin"/></svg>Site Address</div>
    <div class="field" style="top:231px"><svg><use href="#icon-case"/></svg>Job Reference</div>
    <div class="field" style="top:282px"><svg><use href="#icon-calendar"/></svg>Date of Attendance</div>
    <div class="field" style="top:332px"><svg><use href="#icon-user"/></svg>Technician</div>
  </div>
  <div class="cta"><span class="cta__dot"><svg viewBox="0 0 10 10"><path d="M3.5 1.5 L7 5 L3.5 8.5"/></svg></span>Call Us Now</div>
</section>

<!-- Client & site details -->
<section class="page page--client">
  <svg class="page__backdrop" aria-hidden="true"><use href="#backdrop"/></svg>
  <div class="page__photo" role="img" aria-label="Photo of a plumber in navy workwear holding a pipe wrench"></div>
  <div class="brand">TIDEWAY<span class="brand__sub">PLUMBING</span></div>
  <div class="card">
    <h2 class="card__title" style="top:11px">Client &amp; Site<br><span class="accent">Details</span></h2>
    <div class="field" style="top:114px"><svg><use href="#icon-user"/></svg>Client Name</div>
    <div class="field" style="top:163px"><svg><use href="#icon-pin"/></svg>Site Address</div>
    <div class="field" style="top:211px"><svg><use href="#icon-user"/></svg>Contact Person</div>
    <div class="field" style="top:259px"><svg><use href="#icon-user"/></svg>Contact Details</div>
    <div class="group-label" style="top:281px">Access Notes</div>
    <div class="check" style="top:303px">After-Hours</div>
    <div class="check" style="top:322px">Tenant Access</div>
  </div>
  <div class="cta"><span class="cta__dot"><svg viewBox="0 0 10 10"><path d="M3.5 1.5 L7 5 L3.5 8.5"/></svg></span>Call Us Now</div>
</section>

<!-- Reason for attendance -->
<section class="page page--reason">
  <svg class="page__backdrop" aria-hidden="true"><use href="#backdrop"/></svg>
  <div class="page__photo" role="img" aria-label="Photo of a plumber in red shirt and blue overalls holding a red pipe wrench, arms crossed"></div>
  <div class="brand">TIDEWAY<span class="brand__sub">PLUMBING</span></div>
  <div class="card">
    <h2 class="card__title" style="top:14px">Reason For<br><span class="accent">Attendance</span></h2>
    <p class="summary">The client reported a recurring blockage affecting the sanitary drainage servicing multiple fixtures within the tenancy. Intermittent slow drainage and odour concerns were noted.</p>
    <div class="group-label" style="left:18px;top:182px">Type of Attendance</div>
    <div class="check" style="left:18px;top:206px">Reactive</div>
    <div class="check" style="left:18px;top:227px">Scheduled Maintenance</div>
    <div class="check" style="left:18px;top:248px">Investigation</div>
    <div class="check" style="left:18px;top:269px">Emergency</div>
    <div class="field" style="left:16px;top:293px;width:140px"><svg><use href="#icon-doc"/></svg>Reported Issue</div>
  </div>
  <div class="cta"><span class="cta__dot"><svg viewBox="0 0 10 10"><path d="M3.5 1.5 L7 5 L3.5 8.5"/></svg></span>Call Us Now</div>
</section>

</body>
</html>
```